Flyer Tally Your Ledger Free

Hi
Can you please design me a DL Flyer for: Tally Your Ledger Free
Info:
Starting a new Business ?
Want to save on bookkeeping fees for your existing business?

You can now save 1000's off bookkeeping fees by Doing it Yourself.

Using our Bookkeeper software you simply key in the information as you go.

We offer one on one training, backup and support.
We can assist you with BAS Preparation and Payrol Advice.

Add Modules as required:
Point of Sale Module
Jobs Management Module
Website Intergration Module

Fee set up assistance and training.

Lets get the ball rolling: 1300 642 815
www.tylfr.com.au
admin@tylfr.com.au (use the logo thing you made)

Target Market(s)

Small Business

Colors
ec1f27
f04a50
f59296
fcdcdc
ffffff

Requirements
Nice to have
• image/s related to bookkeeping

```html
<!DOCTYPE html>
<html lang="en">
<head>
<meta charset="utf-8">
<title>Tally Your Ledger Free – DL Flyer</title>
<link href="https://fonts.googleapis.com/css2?family=Nunito:wght@400;600;700;800;900&display=swap" rel="stylesheet">
<style>
:root{
  --red:#ec1f27;
  --red-bright:#ff0000;
  --red-soft:#f04a50;
  --pink:#f59296;
  --blush:#fcdcdc;
  --white:#ffffff;
  --ink:#333333;
  --band-grey:#4a4a4a;
  --stage:#5c5c5c;
}
*{margin:0;padding:0;box-sizing:border-box}
html,body{width:1200px;height:1087px;overflow:hidden;background:var(--stage);font-family:"Nunito",sans-serif}
.flyer{position:absolute;top:90px;width:454px;height:908px;background:var(--white);overflow:hidden}
.flyer--front{left:102px}
.flyer--back{left:638px}
.flyer svg.backdrop{position:absolute;left:0;top:0}
.line{position:absolute;left:0;right:0;text-align:center;white-space:nowrap}
.left-line{position:absolute;white-space:nowrap}

/* front */
.brand{position:absolute;top:66px;left:0;right:0;display:flex;align-items:center;justify-content:center;gap:10px;color:var(--red);font-weight:800;font-size:27px}
.brand__dot{width:26px;height:26px;border-radius:50%;background:var(--red)}
.headline-light{top:166px;font-size:42px;font-weight:600;color:var(--white);letter-spacing:.5px}
.headline-bold{top:205px;font-size:42px;font-weight:900;color:var(--white)}
.sub{font-size:20px;font-weight:600;color:var(--white)}
.save-small{top:610px;font-size:30px;font-weight:800;color:var(--white)}
.save-big{top:635px;font-size:60px;font-weight:900;color:var(--white);letter-spacing:1px}
.save-mid{font-size:32px;font-weight:800;color:var(--white)}
.rolling{top:781px;font-size:23px;font-weight:800;color:var(--white);letter-spacing:.5px}
.phone-red{top:824px;font-size:36px;font-weight:900;color:var(--red);display:flex;justify-content:center;align-items:center;gap:10px}
.contacts{top:866px;font-size:15.5px;font-weight:600;color:var(--ink)}
.contacts b{color:var(--red);font-weight:600}

/* back */
.intro{left:44px;font-size:20px;font-weight:600;color:var(--white)}
.intro strong{font-weight:800}
.offer{left:44px;font-size:33px;font-weight:900;color:var(--white)}
.assist{left:44px;font-size:27px;font-weight:900;color:var(--red)}
.module{position:absolute;top:672px;border-left:1.5px solid var(--red);padding-left:12px;height:104px}
.module svg{display:block}
.module__label{margin-top:8px;font-size:17px;line-height:21.5px;color:var(--ink);font-weight:600}
.fee-band{position:absolute;left:0;top:789px;width:454px;height:36px;background:var(--red-bright);color:var(--white);font-weight:900;font-size:17px;text-align:center;line-height:36px;letter-spacing:.3px}
.phone-dark{top:830px;font-size:33px;font-weight:900;color:var(--ink);display:flex;justify-content:center;align-items:center;gap:10px}
.web{top:865px;font-size:22px;font-weight:700;color:var(--ink)}
.web b{color:var(--red);font-weight:700}
</style>
</head>
<body>

<section class="flyer flyer--front">
  <svg class="backdrop" width="454" height="908" viewBox="0 0 454 908">
    <defs>
      <linearGradient id="filesTone" x1="0" y1="0" x2="1" y2="1">
        <stop offset="0" stop-color="#c9c3d9"/>
        <stop offset=".45" stop-color="#6f6b78"/>
        <stop offset=".6" stop-color="#d8d6a6"/>
        <stop offset="1" stop-color="#3a3a40"/>
      </linearGradient>
      <linearGradient id="redFade" x1="0" y1="0" x2="0" y2="1">
        <stop offset="0" stop-color="#ff0000"/>
        <stop offset="1" stop-color="#ec1f27"/>
      </linearGradient>
    </defs>
    <rect x="0" y="0" width="454" height="150" fill="#f4f4f4"/>
    <rect x="0" y="150" width="454" height="622" fill="url(#filesTone)" role="img" aria-label="Photo of stacked office binders labelled Salaries and Payroll"/>
    <polygon points="0,150 454,150 454,293 227,362 0,293" fill="url(#redFade)"/>
    <polygon points="0,624 227,556 454,624 454,772 0,772" fill="var(--red-bright)"/>
    <line x1="150" y1="250" x2="305" y2="250" stroke="#fff" stroke-width="2"/>
    <rect x="0" y="772" width="454" height="42" fill="var(--band-grey)"/>
  </svg>

  <div class="brand"><span class="brand__dot"></span>Tally Your Ledger Free</div>
  <div class="line headline-light">STARTING A</div>
  <div class="line headline-bold">NEW BUSINESS?</div>
  <div class="line sub" style="top:262px">Want to save on bookkeeping fees</div>
  <div class="line sub" style="top:287px">for your existing business?</div>

  <div class="line save-small">You can now Save</div>
  <div class="line save-big">1000's OFF</div>
  <div class="line save-mid" style="top:690px">bookkeeping fees by</div>
  <div class="line save-mid" style="top:726px">Doing it Yourself.</div>

  <div class="line rolling">LETS GET THE BALL ROLLING:</div>
  <div class="line phone-red">
    <svg width="28" height="28" viewBox="0 0 28 28"><circle cx="14" cy="14" r="12.5" fill="none" stroke="var(--red)" stroke-width="2.5"/><path d="M9 8c1-1 2-1 2.5 0l1.5 2.5c.4.7 0 1.3-.6 1.8.8 1.8 2 3 3.5 3.7.5-.6 1.1-1 1.8-.6l2.5 1.5c1 .5 1 1.5 0 2.5-1.5 1.5-4 1.2-7-1.5S7.5 9.5 9 8z" fill="var(--red)"/></svg>
    1300 642 815
  </div>
  <div class="line contacts">✉ admin@tyl<b>fr</b>.com.au &nbsp;|&nbsp; ⊕ www.tyl<b>fr</b>.com.au</div>
</section>

<section class="flyer flyer--back">
  <svg class="backdrop" width="454" height="908" viewBox="0 0 454 908">
    <defs>
      <linearGradient id="officeTone" x1="0" y1="0" x2="1" y2="1">
        <stop offset="0" stop-color="#eeeeec"/>
        <stop offset=".5" stop-color="#d9d2c8"/>
        <stop offset="1" stop-color="#a89a88"/>
      </linearGradient>
    </defs>
    <rect x="0" y="0" width="454" height="908" fill="#f6f6f6"/>
    <polygon points="0,259 454,259 454,575 0,502" fill="url(#officeTone)" role="img" aria-label="Photo of a smiling woman reviewing paperwork at a laptop in a bright office"/>
    <polygon points="0,0 454,0 454,259 0,335" fill="var(--red-bright)"/>
    <line x1="44" y1="130" x2="316" y2="130" stroke="#fff" stroke-width="1.5"/>
  </svg>

  <div class="left-line intro" style="top:44px">Using our <strong>Bookkeeper Software</strong></div>
  <div class="left-line intro" style="top:69px">you simply key in the information</div>
  <div class="left-line intro" style="top:94px">as you go.</div>

  <div class="left-line offer" style="top:143px">We offer</div>
  <div class="left-line offer" style="top:183px">One on one Training,</div>
  <div class="left-line offer" style="top:222px">Backup and Support.</div>

  <div class="left-line assist" style="top:555px">We can assist you</div>
  <div class="left-line assist" style="top:589px">with BAS Preparation and</div>
  <div class="left-line assist" style="top:622px">Payrol Advice.</div>

  <div class="module" style="left:44px">
    <svg width="36" height="36" viewBox="0 0 36 36" fill="none" stroke="var(--red)" stroke-width="1.6"><rect x="4" y="3" width="16" height="13"/><text x="9" y="13" font-size="9" fill="var(--red)" stroke="none">$</text><rect x="2" y="22" width="32" height="11"/><path d="M8 16v6M24 12h6v10"/><path d="M6 27h4M13 27h4M20 27h4"/></svg>
    <div class="module__label">Point of<br>Sale<br>Module</div>
  </div>
  <div class="module" style="left:150px">
    <svg width="36" height="36" viewBox="0 0 36 36" fill="none" stroke="var(--red)" stroke-width="1.6"><path d="M5 3h16l6 6v22H5z"/><path d="M9 12h10M9 17h8M9 22h6"/><circle cx="27" cy="27" r="5"/><circle cx="27" cy="27" r="1.8"/></svg>
    <div class="module__label">Jobs<br>Management<br>Module</div>
  </div>
  <div class="module" style="left:305px">
    <svg width="36" height="36" viewBox="0 0 36 36" fill="none" stroke="var(--red)" stroke-width="1.6"><rect x="2" y="3" width="32" height="24"/><path d="M2 8h32M6 13h10M6 18h14M22 13h8M22 18h8M12 31h12M18 27v4"/></svg>
    <div class="module__label">Website<br>Intergration<br>Module</div>
  </div>

  <div class="fee-band">FEE SET UP ASSISTANCE AND TRAINING</div>
  <div class="line phone-dark">
    <svg width="26" height="26" viewBox="0 0 28 28"><circle cx="14" cy="14" r="12.5" fill="none" stroke="var(--red)" stroke-width="2.5"/><path d="M9 8c1-1 2-1 2.5 0l1.5 2.5c.4.7 0 1.3-.6 1.8.8 1.8 2 3 3.5 3.7.5-.6 1.1-1 1.8-.6l2.5 1.5c1 .5 1 1.5 0 2.5-1.5 1.5-4 1.2-7-1.5S7.5 9.5 9 8z" fill="var(--red)"/></svg>
    1300 642 815
  </div>
  <div class="line web"><span style="color:var(--red)">⊕</span> www.tyl<b>fr</b>.com.au</div>
</section>

</body>
</html>
```